Flyer Design für Kosmetikerin und Visagistin gesucht
Zielgruppe
Ich bin ein Einmannbetrieb und biete Kosmetik für Frauen, Männer und Jugendliche, Visagistik, Nageldesign und Wimpernverlängerun an - eine bestimmte Zielgruppe gibt es eigentlich nicht - es sollen alle angesprochen werden.
Aufgabenstellung
Ich hätte gerne einen Flyer, welcher beidseitig bedruckt wird und welchen ich dann per Postwurfsendung an die Haushalte in meiner Umgebung verteilen kann, da ich gerade mein Kosmetikstudio eröffnet habe. Auf der Vorderseite hätte ich gerne meinen Namen, Dipl. Kosmetikerin, Dipl. Make-up-Artist, Dipl. Nageldesignerin, meine Adresse (eventuell kleine Karte) und meine Telefonnummer mit dem Hinweis 'Termine nach telefonischer Vereinbarung' Und meine Mailadresse.
Weiters hätte ich gerne 'Neueröffnung', 'tolle Eröffnungsangbote bis Jahresende', 'kleines Willkommensgeschenk solange der Vorrat reicht' und den Satz 'der erste Eindruck hat keine zweite Chance' darauf. Ansonsten gilt bei der Vorderseite freie Gestaltung!
Auf der Rückseite hätte ich gerne meine Preisliste - ich lade sie mal als PDF-Datei hoch...
Ich lade auch mein Logo, meine Preisliste und ein paar Bilder hoch, die Bilder dürfen verwendet werden, denn ich habe dafür auch bezahlt - ist aber keine Pflicht - bin für jede andere Idee offen! Bevorzugten Farben sind Rosa und Pink, es darf auch versielt sein! Das Format, ob quer, hochgestellt, gefaltet usw. ist mir eigentlich egal - die Preisliste soll nur gut leserlich sein - kann auch von der Anordnung her verändert werden.

```html
<!DOCTYPE html>
<html lang="de">
<head>
<meta charset="utf-8">
<title>Faltblatt Kosmetikstudio</title>
<link href="https://fonts.googleapis.com/css2?family=Oswald:wght@500;700&family=Roboto+Condensed:wght@300;400;700&family=Ubuntu:wght@400&display=swap" rel="stylesheet">
<style>
  :root{
    --magenta:#a5156f;
    --pink:#d0529b;
    --rose:#f4dfeb;
    --rose-soft:#faeef5;
    --ink:#2a2a2a;
    --paper:#ffffff;
  }
  *{box-sizing:border-box;margin:0;padding:0}
  html,body{width:1200px;height:848px;overflow:hidden;background:var(--paper)}
  body{position:relative;font-family:"Roboto Condensed",sans-serif;color:var(--ink)}
  .board-label{position:absolute;font-family:"Ubuntu",sans-serif;font-size:22px;color:#111}
  .label-front{left:114px;top:30px;transform:rotate(-4deg)}
  .label-back{left:465px;top:95px}
  .label-inner{left:851px;top:22px}
  .spec{position:absolute;left:669px;top:744px;font-family:"Ubuntu",sans-serif;font-size:20px;line-height:23.5px;color:#111}

  .panel{position:absolute;background:var(--paper);box-shadow:0 1px 4px rgba(0,0,0,.25);overflow:hidden}

  /* front */
  .front{left:62px;top:64px;width:240px;height:672px;transform:rotate(-4deg);transform-origin:50% 50%}
  .front::after{content:"";position:absolute;right:0;top:0;width:11px;height:100%;background:var(--magenta)}
  .front-brand{position:absolute;left:16px;top:26px;width:200px;text-align:center}
  .front-brand .name{font-family:"Roboto Condensed",sans-serif;font-weight:400;font-size:30px;color:var(--pink);display:flex;align-items:center;justify-content:center;gap:6px}
  .front-brand .dot{width:12px;height:12px;border-radius:50%;background:var(--pink)}
  .front-brand .tag{font-size:5.5px;letter-spacing:.2px;color:var(--pink);margin-top:4px}
  .hero{position:absolute;left:0;top:110px;width:229px;height:410px;background:linear-gradient(160deg,#5a3a2c 0%,#8a5d48 35%,#d8b49e 60%,#caa08a 80%,#6b4a3a 100%)}
  .quote{position:absolute;left:10px;top:124px;font-family:"Oswald",sans-serif;font-weight:700;font-size:15.5px;line-height:17px;color:#fff;text-transform:uppercase}
  .badge{position:absolute;left:46px;top:418px;width:82px;height:82px;border-radius:50%;background:var(--magenta);color:#fff;font-family:"Oswald",sans-serif;font-weight:500;font-size:11px;line-height:12.5px;display:flex;align-items:center;justify-content:center;text-align:center;transform:rotate(-8deg)}
  .thumbs{position:absolute;left:0;top:520px;width:229px;height:78px;display:flex}
  .thumb{flex:1}
  .thumb-facial{background:linear-gradient(135deg,#d9d4cf,#9c8f86)}
  .thumb-tools{background:linear-gradient(135deg,#d8a9cf,#8e4f8a)}
  .thumb-nails{background:linear-gradient(135deg,#f2e2ea,#c7a3bc)}
  .opening{position:absolute;left:12px;top:604px;width:214px;font-family:"Oswald",sans-serif;font-weight:700;font-size:27px;line-height:30px;color:var(--magenta)}
  .welcome{position:absolute;left:12px;top:634px;width:214px;font-family:"Oswald",sans-serif;font-weight:500;font-size:11.5px;line-height:13px;color:var(--pink);text-align:center}

  /* back */
  .back{left:394px;top:130px;width:238px;height:675px}
  .back::before{content:"";position:absolute;left:0;top:0;width:11px;height:100%;background:var(--magenta)}
  .map{position:absolute;left:23px;top:12px;width:206px;height:142px;border:1px solid #e6bcd4;background:linear-gradient(135deg,#fbf2f7,#f3dbe8)}
  .route{position:absolute;left:0;top:0}
  .back-brand{position:absolute;left:30px;top:206px;width:200px;text-align:center;font-size:18px;color:var(--pink);display:flex;align-items:center;justify-content:center;gap:5px}
  .back-brand .dot{width:9px;height:9px;border-radius:50%;background:var(--pink)}
  .contact{position:absolute;left:11px;top:256px;width:227px;text-align:center;font-size:6.8px;line-height:9.6px}
  .contact .head{color:var(--magenta);font-weight:700}
  .contact .owner{font-weight:700}
  .contact .gap{height:9.6px}
  .appointment{position:absolute;left:61px;top:581px;width:130px;height:72px;border:1px solid #e6bcd4;background:var(--rose-soft);font-size:6.8px;display:flex;align-items:flex-end;justify-content:center;padding-bottom:6px}

  /* inner */
  .inner{left:670px;top:58px;width:477px;height:674px}
  .inner::before,.inner::after{content:"";position:absolute;top:0;height:100%;background:var(--magenta)}
  .inner::before{left:0;width:11px}
  .inner::after{right:0;width:10px}
  .col{position:absolute;top:14px;font-size:6.9px;line-height:9.6px}
  .col-left{left:20px;width:205px}
  .col-right{left:252px;width:205px}
  .sec{margin-bottom:9.6px}
  .sec h3{font-weight:300;font-size:6.9px;color:var(--pink)}
  .row{display:flex;justify-content:space-between;align-items:flex-end}
  .row .p{flex:0 0 34px;text-align:right;white-space:nowrap}
  .relax{position:absolute;left:11px;bottom:0;width:456px;height:120px;background:linear-gradient(180deg,rgba(255,255,255,0) 0%,#f0d9cc 45%,#d9b6a3 100%)}
</style>
</head>
<body>

<div class="board-label label-front">Vorderseite</div>
<div class="board-label label-back">Rückseite</div>
<div class="board-label label-inner">Innenseiten</div>

<!-- front -->
<section class="panel front">
  <div class="front-brand">
    <div class="name"><span class="dot"></span>Belle Atelier by Mira</div>
    <div class="tag">KOSMETIK | VISAGISTIK | NAGELDESIGN | WIMPERNVERLÄNGERUNG</div>
  </div>
  <div class="hero" role="img" aria-label="Porträtfoto einer Frau mit geschminkten Augen"></div>
  <p class="quote">„Der erste Eindruck hat<br>keine zweite Chance“</p>
  <div class="badge">Tolle<br>Eröffnungs-<br>angebote bis<br>Jahresende</div>
  <div class="thumbs">
    <div class="thumb thumb-facial" role="img" aria-label="Foto einer Gesichtsbehandlung"></div>
    <div class="thumb thumb-tools" role="img" aria-label="Foto von Orchidee und Pinseln"></div>
    <div class="thumb thumb-nails" role="img" aria-label="Foto manikürter Hände"></div>
  </div>
  <div class="opening">NEUERÖFFNUNG</div>
  <div class="welcome">Und ein kleines Willkommens-<br>geschenk solange der Vorrat reicht!</div>
</section>

<!-- back -->
<section class="panel back">
  <div class="map" role="img" aria-label="Anfahrtsskizze zum Studio"></div>
  <svg class="route" width="238" height="675" viewBox="0 0 238 675">
    <path d="M144 154 C 140 180, 110 190, 95 215 M78 258 C 60 300, 40 360, 35 420 C 30 480, 50 540, 65 578" fill="none" stroke="var(--magenta)" stroke-width=".8" stroke-dasharray="1.5 2"/>
  </svg>
  <div class="back-brand"><span class="dot"></span>Belle Atelier by Mira</div>
  <div class="contact">
    <div class="head">INHABERIN:</div>
    <div class="owner">Marlene Kofler</div>
    <div>Dipl. Kosmetikerin</div>
    <div>Dipl. Make-up-Artist</div>
    <div>Dipl. Nageldesignerin</div>
    <div class="gap"></div>
    <div>Lindengasse 12/3</div>
    <div>2304 Orth</div>
    <div>Telefon: 0660.5550123</div>
    <div>E-Mail: belle.atelier@mailpost.at</div>
    <div class="gap"></div>
    <div class="head">ÖFFNUNGSZEITEN:</div>
    <div>Termine nach telefonischer Vereinbarung</div>
  </div>
  <div class="appointment">Ihr nächster Termin</div>
</section>

<!-- inner -->
<section class="panel inner">
  <div class="col col-left">
    <div class="sec"><h3>Gesichtsbehandlung für Eilige</h3>
      <div class="row"><span>Reinigung, Hautanalyse, Tonic, Peeling, Maske,<br>Tagespflege</span><span class="p">€ 25,00</span></div></div>
    <div class="sec"><h3>Gesichtsbehandlung klassisch</h3>
      <div class="row"><span>Reinigung, Hautanalyse, Peeling, Dampf, Ausreinigen, Tonic, Maske,<br>Lippenpflege,<br>Massage, Augen- u.Tagespflege</span><span class="p">€ 38,00</span></div></div>
    <div class="sec"><h3>Gesichtsbehandlung deluxe</h3>
      <div class="row"><span>Reinigung, Hautanalyse, Peeling, Wimpern od.<br>Augenbrauen färben, Dampf, Ausreinigen, Tonic,<br>Augenbrauen faconieren, Ampulle, Maske,<br>Lippenpflege, Massage, Augen- und Tagespflege</span><span class="p">€ 52,00</span></div></div>
    <div class="sec"><h3>Gesichtsbehandlung Anti-Age spezial</h3>
      <div class="row"><span>Reinigung, Hautanalyse, Peeling, Dampf,<br>Ausreinigen, Tonic, Ampulle bzw. Serum,<br>Anti-Aging-Spezialmaske od. Collagen-Vlies<br>nach Hauttyp, Lippenpflege, Augenampulle,<br>Massage, Augen- und Antiaging-Tagespflege</span><span class="p">€ 76,00</span></div></div>
    <div class="sec"><h3>Microdermabrasionbehandlung</h3>
      <div class="row"><span>Reinigung, Peeling, Microdermabrasion,<br>Ampulle od. Serum, Maske, Augen- u. Tagespflege</span><span class="p">€ 54,00</span></div>
      <div class="row"><span>Microdermabrasion-Kur 4x mit Wochenabstand</span><span class="p">€ 205,00</span></div></div>
    <div class="sec"><h3>Fruchtsäurebehandlung</h3>
      <div class="row"><span>Reinigung, Peeling, AHA-Fruchtsäuretonic,<br>AHA-Gingkosomengel, Milchsäurevlies,<br>Massage mit Vit.C-Creme, Augen- u. Tagespflege</span><span class="p">€ 58,00</span></div>
      <div class="row"><span>Kur 4x mit Wochenabstand</span><span class="p">€ 220,00</span></div></div>
    <div class="sec"><h3>Microdermabrasion mit Fruchtsäure kombiniert</h3>
      <div class="row"><span>Reinigung, Peeling, Microdermabrasion,<br>AHA-Fruchtsäuretonic, AHA-Gingkosomengel,<br>Milchsäure-Vlies, Massage mit Vit.C-Creme,<br>Augen- und Tagespflege</span><span class="p">€ 105,00</span></div>
      <div class="row"><span>Kur 4x mit Wochenabstand</span><span class="p">€ 410,00</span></div></div>
    <div class="sec"><h3>Aknespezialbehandlung</h3>
      <div class="row"><span>Reinigung, Peeling, Dampf, Ausreinigen,<br>Tonic, Ampulle, Aknespezialmaske,<br>Spezialtagespflege</span><span class="p">€ 38,00</span></div></div>
    <div class="sec"><h3>Pigmentfleckenspezialbehandlung</h3>
      <div class="row"><span>Reinigung, Peeling, Dampf, Spezialserum,<br>Spezialmaske gegen Pigmentflecken,<br>Augenpflege, Spezialtagespflege</span><span class="p">€ 48,00</span></div></div>
    <div class="sec"><h3>Anticouperosespezialbehandlung</h3>
      <div class="row"><span>Reinigung, Peeling, Dampf, Spezialserum,<br>Spezialmaske, Augenpflege, Spezialtagespflege</span><span class="p">€ 48,00</span></div>
      <div class="row"><span>Gesicht-, Hals- und Dekolletemassage (ca 20 min)</span><span class="p">€ 18,00</span></div>
      <div class="row"><span>Kosmetische Lymphdrainage (ca. 30 min)</span><span class="p">€ 23,00</span></div></div>
  </div>

  <div class="col col-right">
    <div class="sec"><h3>Zusatzbehandlungen:</h3>
      <div class="row"><span>Wimpern färben</span><span class="p">€ 6,00</span></div>
      <div class="row"><span>Augenbrauen färben</span><span class="p">€ 5,00</span></div>
      <div class="row"><span>Augenbrauen faconnieren/harzen</span><span class="p">€ 4,00</span></div>
      <div class="row"><span>Augen-Intensivbehandlung</span><span class="p">€ 18,00</span></div>
      <div class="row"><span>Wimperndauerwelle</span><span class="p">€ 18,00</span></div>
      <div class="row"><span>Kinn harzen</span><span class="p">€ 6,00</span></div>
      <div class="row"><span>Oberlippe harzen</span><span class="p">€ 4,00</span></div>
      <div class="row"><span>Wirkstoffampulle</span><span class="p">€ 8,00</span></div>
      <div class="row"><span>Hochfrequenz</span><span class="p">€ 6,00</span></div></div>
    <div class="sec">
      <div class="row"><h3>Cellulite-/Entschlackungswickel</h3><span class="p">€ 32,00</span></div>
      <div class="row"><span>10er Block: 10 + 1 gratis</span><span class="p">€ 320,00</span></div></div>
    <div class="sec"><h3>Hände:</h3>
      <div class="row"><span>Klassische Maniküre mit Pflege oder Farb-Lack</span><span class="p">€ 16,00</span></div>
      <div class="row"><span>Maniküre mit Handpeeling und Paraffinbad</span><span class="p">€ 32,00</span></div>
      <div class="row"><span>Handpeeling + Paraffinbad</span><span class="p">€ 18,00</span></div>
      <div class="row"><span>Permanenter Gel-Lack am Naturnagel</span><span class="p">€ 16,00</span></div>
      <div class="row"><span>French</span><span class="p">€ 2,00</span></div>
      <div class="row"><span>Gellack entfernen mit Pflege</span><span class="p">€ 12,00</span></div></div>
    <div class="sec">
      <div class="row"><span>Nagelmodellage mit Gel</span><span class="p"></span></div>
      <div class="row"><span>Neues Set</span><span class="p">€ 48,00</span></div></div>
    <div class="sec">
      <div class="row"><span>Auffüllen All inclusive (French, Fullcover, Glitzer, Nailart/<br>Steinchen/Airbrush/Sticker auf 2 Finger)</span><span class="p">€ 38,00</span></div>
      <div class="row"><span>Nailart/Steinchen/Airbrush/Sticker zusätzlich pro Finger</span><span class="p">€ 0,50</span></div>
      <div class="row"><span>Modellage entfernen mit Pflege</span><span class="p">€ 16,00</span></div></div>
    <div class="sec"><h3>Permanente Wimpernverlängerung</h3>
      <div class="row"><span>erstes Set</span><span class="p">€ 115,00</span></div>
      <div class="row"><span>Auffüllen innerhalb von 3 Wochen</span><span class="p">€ 40,00</span></div>
      <div class="row"><span>Innerhalb von 4-5 Wochen</span><span class="p">€ 50,00</span></div></div>
    <div class="sec"><h3>Enthaarung:</h3>
      <div class="row"><span>Beine harzen inkl. Knie</span><span class="p">€ 18,00</span></div>
      <div class="row"><span>Beine komplett harzen</span><span class="p">€ 28,00</span></div>
      <div class="row"><span>Achseln harzen</span><span class="p">€ 11,00</span></div>
      <div class="row"><span>Bikinizone harzen</span><span class="p">€ 12,00</span></div>
      <div class="row"><span>Arme harzen</span><span class="p">€ 22,00</span></div>
      <div class="row"><span>Harzpackage klein (Beine inkl. Knie, Achseln, Bikinizone)</span><span class="p">€ 38,00</span></div>
      <div class="row"><span>Harzpackage groß (Beine, Achseln, Bikinizone, Arme)</span><span class="p">€ 68,00</span></div>
      <div class="row"><span>Männer: Rücken harzen</span><span class="p">€ 26,00</span></div>
      <div class="row"><span>Brust u. Bauch harzen</span><span class="p">€ 26,00</span></div></div>
    <div class="sec"><h3>Make up:</h3>
      <div class="row"><span>Dezentes Tagesmake up</span><span class="p">€ 22,00</span></div>
      <div class="row"><span>Abendmake up</span><span class="p">€ 26,00</span></div>
      <div class="row"><span>Hochzeitsmake up inkl. 1 Probetermin</span><span class="p">€ 48,00</span></div>
      <div class="row"><span>Brautpackage (Probe-Make up, Make up am Tag<br>der Hochzeit, Nagelmodellage, Wimpernverlängerung)</span><span class="p">€ 199,00</span></div></div>
  </div>
  <div class="relax" role="img" aria-label="Foto einer entspannten Frau bei der Gesichtsbehandlung"></div>
</section>

<div class="spec">Faltblatt | Einbruchfalz<br>DIN A5 lang | 10,5 x 29,7 cm<br>4seitig<br>4/4-farbig</div>

</body>
</html>
```